Establishing a website for a non profit organisation

The foundation is called:

German: Edle Alte Bruderschaft des Hofes Lindenmark e.V.

Englisch (Translation): Noble old Brotherhood of Court Lindenmark e.V.

The foundation is a legal nonprofit organization with the purpose to help people in need. The foundation - a charitable organization - donates funds and supports solely and directly people living in Frankfurt and in Germany.

In some cases the foundation works together with other charitable organizations that support projects to help people in need.

The foundation also functions as trustee with powers of administration of property in trust with a legal obligation to administer it solely for the purposes specified. The purpose is not to generate/obtain wealth for shareholders but to respectfully execute the benevolent intentions of the founders/testators in the interest of the legatee.

The foundation was established in 1408.

The website should give a good and easy overview about the foundation work.
It should be easy to figure out how to participate and help the organisation.
Either you can participate with a one time donation, with a regular donation or with a testament.

For those with donation it is possible to hand over an contribution receipt for tax purposes.

The main color should be red: RGB R:229 - G:47 - B:34

```html
<!DOCTYPE html>
<html lang="en">
<head>
<meta charset="utf-8">
<title>Noble old Brotherhood of Court Lindenmark e.V.</title>
<link href="https://fonts.googleapis.com/css2?family=Source+Sans+3:wght@400;600;700&display=swap" rel="stylesheet">
<style>
:root{
  --red:#e52f22;
  --red-dark:#c8261b;
  --ink:#2b2b2b;
  --text:#666;
  --grey-bg:#f2f2f2;
  --line:#dcdcdc;
  --dark:#333;
  --footer:#363636;
  --yellow:#f6d215;
}
*{box-sizing:border-box;margin:0;padding:0}
html,body{width:1200px;height:3127px;overflow:hidden;background:#fff}
body{font-family:"Source Sans 3",Arial,sans-serif;color:var(--ink);position:relative}
p{font-size:15px;line-height:27px;color:var(--text)}

/* header */
.site-header{position:absolute;top:0;left:0;width:1200px;height:169px}
.brand{position:absolute;left:86px;top:56px;font-size:30px;line-height:48px;font-weight:400;letter-spacing:.5px}
.brand .line2{color:var(--red)}
.donate-now{position:absolute;left:968px;top:35px;width:144px;height:40px;background:var(--dark);color:#fff;font-size:17px;font-weight:600;display:flex;align-items:center;justify-content:center;border-radius:2px}
.search{position:absolute;left:853px;top:102px;width:259px;height:35px;border:1px solid #ccc;font-size:14px;color:#999;padding:0 12px;display:flex;align-items:center;justify-content:space-between}

/* nav */
.main-nav{position:absolute;top:169px;left:0;width:1200px;height:58px;background:linear-gradient(#ec3a2c,var(--red-dark));display:flex;padding-left:86px}
.main-nav a{color:#fff;text-decoration:none;font-size:17px;display:flex;align-items:center;justify-content:center;border-right:1px solid rgba(0,0,0,.15)}
.main-nav a.active{background:#b9241a}

/* hero */
.hero{position:absolute;top:227px;left:0;width:1200px;height:470px;background:radial-gradient(ellipse at 55% 40%,#d9b39a 0%,#a77b62 35%,#5b4a48 70%,#3b3638 100%)}
.hero-caption{position:absolute;left:81px;top:218px;width:494px;height:139px;background:rgba(40,40,40,.7);padding:22px 24px;color:#fff}
.hero-caption h1{font-size:30px;font-weight:600;line-height:38px}
.hero-caption p{color:#fff;font-size:15px;line-height:24px;margin-top:6px}
.dots{position:absolute;left:558px;top:438px;display:flex;gap:6px}
.dots span{width:15px;height:15px;border-radius:50%;background:#ccc}
.dots span:first-child{background:#fff}

/* features */
.feature{position:absolute;top:776px;width:180px}
.feature .icon{position:absolute;left:-127px;top:4px;width:106px;height:106px;border-radius:50%;border:3px solid #e6e6e6;background:#f5f5f5;display:flex;align-items:center;justify-content:center}
.feature h2{font-size:22px;font-weight:400;margin-bottom:4px}
.feature p{font-size:14px;line-height:26px}

/* donation */
.divider-shadow{position:absolute;top:960px;left:200px;width:800px;height:14px;background:radial-gradient(ellipse at 50% 0,rgba(0,0,0,.12),rgba(0,0,0,0) 70%)}
.thanks{position:absolute;top:1022px;right:690px;text-align:right}
.thanks h2{font-size:32px;font-weight:400}
.thanks .sub{font-size:22px;color:#444;line-height:40px}
.thanks .amount{font-size:32px;font-weight:600}
.thanks .amount small{font-size:22px;font-weight:400}
.vsep{position:absolute;left:544px;top:1032px;width:1px;height:110px;background:var(--line)}
.donate-options{position:absolute;left:642px;top:1030px}
.donate-options h2{font-size:35px;font-weight:400}
.btn{position:absolute;top:68px;height:42px;display:flex;align-items:center;justify-content:center;font-size:19px}
.btn.life{left:-56px;width:167px;background:var(--dark);color:#fff}
.btn.once{left:134px;width:213px;background:var(--yellow);color:var(--ink);border-bottom:3px solid #d7b30a}
.progress{position:absolute;left:190px;top:1207px;width:790px;height:17px;border-radius:9px;background:linear-gradient(#e4e4e4,#cfcfcf);overflow:hidden}
.progress .fill{width:246px;height:100%;background:repeating-linear-gradient(90deg,var(--red) 0 33px,#fff 33px 35px)}

/* info band */
.info-band{position:absolute;top:1302px;left:0;width:1200px;height:452px;background:var(--grey-bg)}
.info-col{position:absolute;top:68px;width:300px}
.info-col h2{font-size:22px;font-weight:600;letter-spacing:.3px;margin-bottom:26px}
.thumb{width:294px;height:151px}
.info-col h3{font-size:20px;font-weight:400;color:var(--red);margin:18px 0 6px}
.news-item h3{margin:0 0 6px;font-size:18px}
.news-item .date{font-size:14px;color:#777;margin-bottom:4px}
.news-item p{font-size:14px;line-height:24px}
.news-sep{height:1px;background:var(--line);margin:18px 0 22px}

/* history */
.history-title{position:absolute;top:1810px;width:1200px;text-align:center;font-size:37px;font-weight:400}
.timeline-line{position:absolute;left:590px;top:1900px;width:3px;height:800px;background:#555}
.tick{position:absolute;left:574px;width:36px;height:36px;border-radius:50%;background:var(--dark);border:3px solid #fff;box-shadow:0 0 0 1px #555;display:flex;align-items:center;justify-content:center}
.node-dot{position:absolute;left:587px;width:9px;height:9px;border-radius:50%;background:#555}
.date-tag{position:absolute;width:146px;height:44px;background:var(--red);color:#fff;font-size:20px;display:flex;align-items:center;justify-content:center}
.date-tag.left::after{content:"";position:absolute;right:-10px;top:12px;border-left:10px solid var(--red);border-top:10px solid transparent;border-bottom:10px solid transparent}
.date-tag.right::before{content:"";position:absolute;left:-10px;top:12px;border-right:10px solid var(--red);border-top:10px solid transparent;border-bottom:10px solid transparent}
.event{position:absolute;width:460px}
.event h3{font-size:24px;font-weight:400;color:var(--red);line-height:32px}
.event .kicker{font-size:14px;font-weight:600;color:var(--ink);margin:2px 0 10px}
.event p{font-size:14px;line-height:26px}

/* footer */
.site-footer{position:absolute;top:2776px;left:0;width:1200px;height:351px;background:var(--footer);color:#fff}
.foot-col{position:absolute;top:44px}
.foot-col h2{font-size:22px;font-weight:400;margin-bottom:18px}
.foot-col li{list-style:none;font-size:14px;line-height:28px}
.contact li{display:flex;align-items:center;gap:16px}
.foot-col p{color:#fff;font-size:14px;line-height:28px}
.social{display:flex;gap:8px;margin-top:16px}
.social span{width:30px;height:30px;border-radius:50%;background:#fff}
.news-input{width:250px;height:36px;background:#fff;margin-top:18px}
.subscribe{width:120px;height:36px;background:#2b90d9;color:#fff;font-size:16px;display:flex;align-items:center;justify-content:center;margin:16px 0 0 130px}
.foot-rule{position:absolute;left:0;top:266px;width:1200px;height:1px;background:#4a4a4a}
.copyright{position:absolute;left:86px;top:296px;font-size:14px}
</style>
</head>
<body>

<header class="site-header">
  <div class="brand">NOBLE OLD BROTHERHOOD<br><span class="line2">OF COURT LINDENMARK E.V.</span></div>
  <div class="donate-now">DONATE NOW</div>
  <div class="search">Search..
    <svg width="14" height="14" viewBox="0 0 14 14"><circle cx="6" cy="6" r="4.5" fill="none" stroke="#999" stroke-width="1.6"/><line x1="9.3" y1="9.3" x2="13" y2="13" stroke="#999" stroke-width="1.8"/></svg>
  </div>
</header>

<nav class="main-nav">
  <a class="active" style="width:125px">HOME</a>
  <a style="width:106px">EVENTS</a>
  <a style="width:123px">HISTORY</a>
  <a style="width:218px">RECEIVE DONATIONS</a>
  <a style="width:95px">NEWS</a>
  <a style="width:220px">WHAT WE DO TODAY</a>
  <a style="width:127px">CONTACT</a>
</nav>

<section class="hero" role="img" aria-label="Photograph of children looking into the camera">
  <div class="hero-caption">
    <h1>CONSECTETUER ADIPISCING ELIT</h1>
    <p>Lorem ipsum dolor sit amet, consectetuer adipiscing elit, sed diam nonummy nibh euismod tincidunt ut laoreet dolore magna.</p>
  </div>
  <div class="dots"><span></span><span></span><span></span><span></span></div>
</section>

<section class="features">
  <div class="feature" style="left:213px">
    <div class="icon"><svg width="50" height="40" viewBox="0 0 50 40"><polygon points="25,2 48,13 25,24 2,13" fill="#e52f22"/><path d="M11 18v10c0 5 28 5 28 0V18l-14 7z" fill="#e52f22"/><rect x="44" y="13" width="2" height="14" fill="#e52f22"/></svg></div>
    <h2>Education</h2>
    <p>Claritas est etiam processna micus, qui sequitur mutaem consuetudium lectorum</p>
  </div>
  <div class="feature" style="left:572px">
    <div class="icon"><svg width="46" height="42" viewBox="0 0 46 42"><rect x="15" y="2" width="16" height="8" rx="2" fill="none" stroke="#e52f22" stroke-width="3"/><rect x="2" y="9" width="42" height="31" rx="4" fill="#e52f22"/><rect x="19" y="15" width="8" height="19" fill="#fff"/><rect x="13" y="21" width="20" height="7" fill="#fff"/></svg></div>
    <h2>Health</h2>
    <p>Claritas est etiam processna micus, qui sequitur mutaem consuetudium lectorum</p>
  </div>
  <div class="feature" style="left:936px">
    <div class="icon"><svg width="46" height="46" viewBox="0 0 46 46"><path d="M2 22a21 19 0 0 1 42 0z" fill="#e52f22"/><path d="M23 22v16a4 4 0 0 1-8 0" fill="none" stroke="#e52f22" stroke-width="3"/></svg></div>
    <h2>Protect</h2>
    <p>Claritas est etiam processna micus, qui sequitur mutaem consuetudium lectorum</p>
  </div>
</section>

<div class="divider-shadow"></div>

<section class="donation">
  <div class="thanks">
    <h2>Thank you!</h2>
    <div class="sub">You've helped us raise a staggering</div>
    <div class="amount">£70.000 <small>so far!</small></div>
  </div>
  <div class="vsep"></div>
  <div class="donate-options">
    <h2>Posibilities to donate</h2>
    <div class="btn life">LIFE TIME</div>
    <div class="btn once">ONE TIME OPTIONS</div>
  </div>
  <div class="progress"><div class="fill"></div></div>
</section>

<section class="info-band">
  <div class="info-col" style="left:86px">
    <h2>WHAT WE DO TODAY</h2>
    <div class="thumb" role="img" aria-label="Photograph of people in suits talking at a meeting" style="background:linear-gradient(135deg,#6d7680,#3e4650 55%,#8a8f96)"></div>
    <h3>Vivamus sagittis lacus</h3>
    <p>Lasodiaer leroas accntium reseknite riasesa In veveritati etchcto beatae vitae dictiuntaxplic ver sa. Nemo ispemadit aut.</p>
  </div>
  <div class="info-col" style="left:443px">
    <h2>RECEIVE DONATIONS</h2>
    <div class="thumb" role="img" aria-label="Photograph of a smiling child holding a thank-you sign" style="background:linear-gradient(135deg,#c8584a,#e8b48c 50%,#7ea04a)"></div>
    <h3>Aoreet lacus incididunt</h3>
    <p>Lasodiaer leroas accntium reseknite riasesa In veveritati etchcto beatae vitae dictiuntaxplic ver sa. Nemo ispemadit aut.</p>
  </div>
  <div class="info-col" style="left:802px">
    <h2>LATEST NEWS</h2>
    <div class="news-item">
      <h3>Typi non habent claritatem insitam;</h3>
      <div class="date">26/11/2013</div>
      <p>Typi non habent claritatem insitam; est usislegen tis in iis qui facit eorum claritatem Investigatines.</p>
    </div>
    <div class="news-sep"></div>
    <div class="news-item">
      <h3>Typi non habent claritatem insitam;</h3>
      <div class="date">26/11/2013</div>
      <p>Typi non habent claritatem insitam; est usislegen tis in iis qui facit eorum claritatem Investigatines.</p>
    </div>
  </div>
</section>

<section class="history">
  <h2 class="history-title">History of the foundation</h2>
  <div class="timeline-line"></div>

  <div class="node-dot" style="top:1960px"></div>
  <div class="node-dot" style="top:2146px"></div>
  <div class="node-dot" style="top:2348px"></div>
  <div class="node-dot" style="top:2545px"></div>

  <div class="tick" style="top:1975px"><svg width="16" height="14" viewBox="0 0 16 14"><path d="M2 7l4 4 8-9" fill="none" stroke="#fff" stroke-width="3"/></svg></div>
  <div class="tick" style="top:2160px"><svg width="16" height="14" viewBox="0 0 16 14"><path d="M2 7l4 4 8-9" fill="none" stroke="#fff" stroke-width="3"/></svg></div>
  <div class="tick" style="top:2362px"><svg width="16" height="14" viewBox="0 0 16 14"><path d="M2 7l4 4 8-9" fill="none" stroke="#fff" stroke-width="3"/></svg></div>
  <div class="tick" style="top:2559px"><svg width="16" height="14" viewBox="0 0 16 14"><path d="M2 7l4 4 8-9" fill="none" stroke="#fff" stroke-width="3"/></svg></div>

  <div class="date-tag left" style="left:382px;top:1974px">2014 Aug</div>
  <div class="date-tag right" style="left:644px;top:2157px">1993 Aug</div>
  <div class="date-tag left" style="left:382px;top:2359px">1884 June</div>
  <div class="date-tag right" style="left:644px;top:2556px">1403 Oct</div>

  <div class="event" style="left:640px;top:1918px">
    <h3>Hasellus sodales vulputate</h3>
    <div class="kicker">vitae sodales massa</div>
    <p>Donec ultrices faucibus rutrum. Phasellus sodales vulputate urna, vel accum san augue egestas ac. Donec vitae leo at sem lobortis porttitor eu consequat risus. Mauris sed congue orci. Vestibulum gravida nulla nec justo.</p>
  </div>
  <div class="event" style="left:86px;top:2116px">
    <h3>Hasellus sodales vulputate</h3>
    <div class="kicker">vitae sodales massa</div>
    <p>Donec ultrices faucibus rutrum. Phasellus sodales vulputate urna, vel am san augue egestas ac. Donec vitae leo at sem lobortis porttitor eu congat risus. Mauris sed congue orci. Vestibulum gravida nulla ne.</p>
  </div>
  <div class="event" style="left:640px;top:2320px">
    <h3>Hasellus sodales vulputate</h3>
    <div class="kicker">vitae sodales massa</div>
    <p>Donec ultrices faucibus rutrum. Phasellus sodales vulputate urna, vel accum san augue egestas ac. Donec vitae leo at sem lobortis porttitor eu consequat risus. Mauris sed congue orci. Vestibulum gravida nulla nec justo .</p>
  </div>
  <div class="event" style="left:86px;top:2535px">
    <h3>Hasellus sodales vulputate</h3>
    <div class="kicker">vitae sodales massa</div>
    <p>Donec ultrices faucibus rutrum. Phasellus sodales vulputate urna, vel am san augue egestas ac. Donec vitae leo at sem lobortis porttitor eu congat risus. Mauris sed congue orci. Vestibulum gravida nulla nec.</p>
  </div>
</section>

<footer class="site-footer">
  <div class="foot-col" style="left:86px">
    <h2>Downloads</h2>
    <ul>
      <li>Duis autem vel</li>
      <li>Eodem modo typi</li>
      <li>validations and verifiion</li>
      <li>System monitoring</li>
      <li>Emergency Breakdowns</li>
    </ul>
  </div>
  <div class="foot-col contact" style="left:331px">
    <h2>Contact Us</h2>
    <ul>
      <li><svg width="12" height="16" viewBox="0 0 12 16"><path d="M6 0a6 6 0 0 0-6 6c0 4 6 10 6 10s6-6 6-10a6 6 0 0 0-6-6z" fill="#bbb"/><circle cx="6" cy="6" r="2.2" fill="#363636"/></svg>240 Linden Hall Road</li>
      <li><span style="width:12px"></span>Harbor City NY 11001</li>
      <li><svg width="14" height="10" viewBox="0 0 14 10"><rect width="14" height="10" fill="#bbb"/><path d="M0 0l7 6 7-6" fill="none" stroke="#363636" stroke-width="1.4"/></svg>info@lindenmark-ev.org</li>
      <li><svg width="13" height="13" viewBox="0 0 13 13"><path d="M2 0l3 3-1.5 2a8 8 0 0 0 4.5 4.5L10 8l3 3-2 2C5 13 0 8 0 2z" fill="#bbb"/></svg>89 455 2107</li>
    </ul>
  </div>
  <div class="foot-col" style="left:586px;width:220px">
    <h2>Follow Us</h2>
    <p>Follow us our news and events through social networks.</p>
    <div class="social"><span></span><span></span><span></span><span></span></div>
  </div>
  <div class="foot-col" style="left:860px;width:260px">
    <h2>Newsletter</h2>
    <p>Stay in touch with us by signing up for our quarterly newsletter!</p>
    <div class="news-input"></div>
    <div class="subscribe">SUBSCRIBE</div>
  </div>
  <div class="foot-rule"></div>
  <div class="copyright">Copyright ©2013. All Rights Reserved.</div>
</footer>

</body>
</html>
```